Hollow Breeze - New Product needs a Label

We need a package label for a new project that will come to market soon. The company is based in Canada and will need to show 'Made in Canada' with a Canadian flag.

The product is called Hollow Breeze. It is an odour eliminator. It will be in a dark brown plastic container that can be opened and left open in a room.

It can be used to help eliminate a number of different types of smoke; cigarette, pot or even fireplace smoke. We believe that 'no one should know what you smoke'.

We would like to see designs that reflect the intent of the product - to cover smoke. So far we've only thought that smokey colours like smokey green, smokey lavender and smokey grey or other grey tone colours would make sense. Update: I have removed the image that I 'doodled' on my own because I think it's been taken too literally. Please give me a fresh look at what an odor eliminator image could be.

Label dimensions are 11.25"x2.25"
Key wording:

Product Name: Hollow Breeze
Tag line: No one needs to know what you smoke
Also needs to include:
Directions
Remove the lid and place the container in any room where smoke is present. The contents will evaporate, neutralizing odours.

Net Wt. 14 0z. - 400 G
A spot for adding a bar code for scanners

Target Market(s)

Cigarette smokers / pot smokers / people with fire places or people who share a home with any of those categories

Requirements
Must have
• a label that fits the dimensions 11.25"x2.25" and the text / components outlined in the description
Nice to have
• A bit of humour, a sense of natural products

```html
<!DOCTYPE html>
<html lang="en">
<head>
<meta charset="utf-8">
<title>Hollow Breeze – Odour Eliminator Label</title>
<link href="https://fonts.googleapis.com/css2?family=Montserrat:ital,wght@0,300;0,400;0,700;0,800;1,700;1,800&family=Libre+Franklin:wght@400;700;900&display=swap" rel="stylesheet">
<style>
  :root{
    --page:#3a3a3b;
    --ink-black:#060507;
    --plum-deep:#2a0e3d;
    --plum:#4a1f66;
    --plum-mid:#5e2c80;
    --lavender:#a57bc4;
    --white:#ffffff;
    --badge-red:#d8232a;
  }
  *{margin:0;padding:0;box-sizing:border-box}
  html,body{width:1200px;height:1058px;overflow:hidden;background:var(--page)}
  .canvas{position:relative;width:1200px;height:1058px}
  .label{
    position:absolute;left:50px;top:419px;width:1100px;height:220px;overflow:hidden;
    background:linear-gradient(90deg,var(--ink-black) 0%,#120a18 22%,#2c1240 42%,var(--plum) 58%,var(--plum-mid) 72%,var(--plum) 86%,#3a1652 100%);
    box-shadow:0 4px 10px rgba(0,0,0,.45);
    font-family:"Montserrat",sans-serif;color:var(--white);
  }
  .smoke-haze{
    position:absolute;inset:0;
    background:
      radial-gradient(ellipse 200px 60px at 170px 210px,rgba(150,90,190,.45),transparent 70%),
      radial-gradient(ellipse 220px 120px at 560px 90px,rgba(160,110,200,.35),transparent 70%),
      radial-gradient(ellipse 160px 90px at 930px 140px,rgba(170,120,210,.3),transparent 70%);
  }
  .wave{position:absolute;inset:0}
  .directions{
    position:absolute;left:94px;top:46px;width:240px;text-align:center;
    font-size:11px;line-height:13px;font-weight:400;
  }
  .barcode-spot{position:absolute;left:79px;top:137px;width:119px;height:54px;background:var(--white)}
  .origin-badge{
    position:absolute;left:218px;top:127px;width:68px;height:68px;border-radius:50%;
    background:var(--white);border:8px solid var(--badge-red);
  }
  .product-name{
    position:absolute;left:380px;top:24px;font-weight:700;line-height:1;
    text-shadow:2px 3px 4px rgba(0,0,0,.55);
  }
  .product-name .line-one{display:block;font-size:56px;letter-spacing:1px}
  .product-name .line-two{display:block;font-size:46px;margin-top:-3px}
  .name-rule{position:absolute;left:382px;top:125px;width:170px;height:1.5px;background:var(--white)}
  .descriptor{
    position:absolute;left:382px;top:129px;font-size:17px;font-weight:300;line-height:18px;letter-spacing:.3px;
  }
  .tagline{
    position:absolute;right:392px;top:140px;text-align:right;
    font-style:italic;font-weight:800;font-size:12px;line-height:14px;
  }
  .net-rule{position:absolute;left:572px;top:190px;width:136px;height:1.5px;background:var(--white)}
  .net-weight{
    position:absolute;right:392px;top:195px;font-style:italic;font-weight:800;font-size:12px;
  }
  .nutrition{
    position:absolute;left:794px;top:31px;width:262px;height:155px;border:1px solid var(--white);
    padding:2px 3px;font-family:"Libre Franklin",sans-serif;font-size:5.5px;line-height:7px;
  }
  .nutrition h2{font-weight:900;font-size:20px;line-height:21px;border-bottom:1px solid var(--white)}
  .nutrition .row{display:flex;justify-content:space-between;border-bottom:.5px solid rgba(255,255,255,.7)}
  .nutrition .bold{font-weight:700}
  .nutrition .thick{border-bottom:4px solid var(--white)}
  .nutrition .calories{font-weight:900;font-size:11px;line-height:14px;border-bottom:2px solid var(--white)}
  .nutrition .indent{padding-left:8px}
  .nutrition .indent2{padding-left:16px}
</style>
</head>
<body>
<div class="canvas">
  <section class="label">
    <div class="smoke-haze" role="img" aria-label="Drifting lavender smoke photograph across the label"></div>
    <svg class="wave" viewBox="0 0 1100 220" preserveAspectRatio="none" aria-hidden="true">
      <path d="M560 220 C620 200 650 150 700 115 C740 90 770 84 780 83 L780 220 Z" fill="#2c0e40" opacity=".85"/>
      <path d="M780 0 L1100 0 L1100 220 L780 220 Z" fill="#2a0e3d" opacity=".35"/>
      <path d="M640 160 C680 120 720 95 780 83 L780 92 C730 100 690 122 650 160 Z" fill="#a57bc4"/>
    </svg>
    <p class="directions">Directions<br>Remove the lid and place the container in any room where smoke is present. The contents will evaporate, neutralizing odours.</p>
    <div class="barcode-spot" aria-label="Barcode area"></div>
    <div class="origin-badge" aria-label="Origin badge"></div>
    <h1 class="product-name"><span class="line-one">HOLLOW</span><span class="line-two">BREEZE</span></h1>
    <div class="name-rule"></div>
    <p class="descriptor">ODOUR<br>ELIMINATOR</p>
    <p class="tagline">NO ONE NEEDS<br>TO KNOW WHAT<br>YOU SMOKE</p>
    <div class="net-rule"></div>
    <p class="net-weight">Net Wt. 14 0z. - 400 G</p>
    <div class="nutrition">
      <h2>Nutrition Facts</h2>
      <div>4 servings per container/6 raciones por envase</div>
      <div class="row thick bold"><span>Serving size</span><span>1 cup/1 taza (180g)</span></div>
      <div class="bold">Amount per serving/Cantidad por porción</div>
      <div class="row calories"><span>Calories/Calorías</span><span>245</span></div>
      <div class="row bold"><span></span><span>% Daily Value*/% Valor diario*</span></div>
      <div class="row"><span class="bold">Total Fat/Grasa total 12g</span><span>14%</span></div>
      <div class="row indent"><span>Saturated Fat/Grasa Saturada 2g</span><span>10%</span></div>
      <div class="row indent"><span>Trans Fat/Grasa Trans 0g</span><span></span></div>
      <div class="row"><span class="bold">Cholesterol/Colesterol 8mg</span><span>3%</span></div>
      <div class="row"><span class="bold">Sodium/Sodio 210mg</span><span>9%</span></div>
      <div class="row"><span class="bold">Total Carbohydrate/Carbohidrato Total 34g</span><span>12%</span></div>
      <div class="row indent"><span>Dietary Fiber/Fibra Dietética 7g</span><span>25%</span></div>
      <div class="row indent"><span>Total Sugars/Azúcares Totales 5g</span><span></span></div>
      <div class="row indent2"><span>Includes 4g Added Sugars/Incluye 4 g de azúcares añadidos</span><span>8%</span></div>
    </div>
  </section>
</div>
</body>
</html>
```